Our business deals with residential and commercial property management. We have commercial tenants willing to offer deals to our residential tenants. We want a very nice looking card stock where I can add (later) each specific deal/incentive. The template attached has two options but feel free to come up with what you think looks best. We need or logo and possibly this simple phrase as the title,

"Welcome to the Brelford Community!" OR "Join the Brelford Community"

This is optional, use discretion on what is should say:

"Every member of Brelford Commercial is important to us, be a part of our community and explore your neighborhood."

www.brelfordcommercial.example can give you a feel for our look and image. I was thinking of maybe a red & black color scheme.

***Each slot for the deal should be blank so I can add and change each deal later. These are going to be cut out so maybe the "-----" lines around the deals would look good. Thanks!!

Target Market(s)

Residential Tenants: Single & Multi Families

Industry/Entity Type

Property Management

Font styles to use
Serif

Colors
ec1f27
000000
fbfbfb

Requirements
Must have
• -Logo (Attached)
• -6 blank slots to add deals later (Can have more deals based on appropriate look)
• -either "Welcome to the Brelford Community" or "Join the Brelford Community"
• -Our phone number: 801.555.0147
• -Website: www.brelfordcommercial.example
• -Address: 417 E. Dunmore Way Suite 5, Centerville, UT 84099
Nice to have
• "Every member of Brelford Commercial is important to us, be a part of our community and explore your neighborhood."
• This could be something else that's similar but sounds better.
• Possible color options: red, black, white OR Your discretion.
Should not have
• Pictures of properties or people.

```html
<!DOCTYPE html>
<html lang="en">
<head>
<meta charset="utf-8">
<title>Join the Brelford Community</title>
<link rel="stylesheet" href="https://fonts.googleapis.com/css2?family=Tinos:ital,wght@0,400;0,700;1,700&family=Open+Sans:wght@400;700&display=swap">
<style>
  :root {
    --red: #ec1f27;
    --deep-red: #9c1b21;
    --dark-red: #7a1419;
    --mid-red: #b3232a;
    --black: #000000;
    --paper: #fbfbfb;
    --ink: #1a1a1a;
  }
  * { box-sizing: border-box; margin: 0; padding: 0; }
  html, body { width: 849px; height: 1200px; overflow: hidden; background: var(--paper); }
  .flyer { position: relative; width: 849px; height: 1200px; background: var(--paper); overflow: hidden; font-family: "Tinos", serif; color: var(--ink); }
  .decor { position: absolute; inset: 0; width: 849px; height: 1200px; }

  .brand { position: absolute; right: 32px; top: 160px; display: flex; align-items: center; gap: 14px; }
  .brand-mark { width: 26px; height: 26px; background: var(--red); }
  .brand-name { font-family: "Tinos", serif; font-weight: 700; font-size: 46px; line-height: 1; color: var(--red); }

  .title-banner { position: absolute; left: 0; top: 262px; width: 560px; height: 62px; background: var(--deep-red); clip-path: polygon(0 0, 100% 0, 96% 100%, 0 100%); }
  .title-banner h1 { position: absolute; left: 10px; top: 8px; right: 34px; bottom: 8px; border: 2px solid var(--paper); border-left: none; display: flex; align-items: center; padding-left: 22px; font-weight: 400; font-size: 33px; color: var(--paper); }

  .tagline { position: absolute; left: 120px; right: 40px; top: 352px; text-align: center; font-style: italic; font-weight: 700; font-size: 22px; line-height: 1.4; color: var(--black); }

  .deal { position: absolute; color: var(--paper); font-size: 16px; line-height: 1.3; background: linear-gradient(160deg, var(--mid-red) 0%, var(--deep-red) 55%, var(--dark-red) 100%); }
  .deal-row-1 { top: 440px; height: 170px; }
  .deal-row-1.deal { clip-path: polygon(0 22%, 100% 0, 100% 100%, 0 88%); padding: 50px 14px 0 14px; }
  .deal-row-2 { top: 640px; height: 150px; }
  .deal-row-2.deal { clip-path: polygon(8% 0, 100% 12%, 92% 100%, 0 88%); padding: 44px 22px 0 22px; text-align: center; }
  .deal-col-1 { left: 34px; width: 180px; }
  .deal-col-2 { left: 232px; width: 186px; }
  .deal-col-3 { left: 428px; width: 188px; }
  .deal-col-4 { left: 630px; width: 190px; }
  .deal-row-1.deal-col-2 { padding-left: 60px; }
  .deal-row-1.deal-col-4 { padding-left: 70px; }
  .deal .saving { display: block; margin-top: 14px; }
  .deal-partner { display: flex; gap: 10px; text-align: left; padding-left: 28px !important; }
  .partner-name { width: 58px; font-size: 14px; }
  .partner-badge { display: block; width: 52px; height: 22px; margin-top: 6px; background: var(--paper); }

  .section-tab { position: absolute; top: 850px; height: 42px; background: var(--deep-red); color: var(--paper); font-family: "Open Sans", sans-serif; font-weight: 700; font-size: 20px; display: flex; align-items: center; }
  .deals-tab { left: 42px; width: 240px; padding-left: 16px; clip-path: polygon(0 0, 100% 0, 94% 100%, 0 100%); }
  .contact-tab { left: 495px; width: 312px; justify-content: center; clip-path: polygon(4% 0, 100% 0, 100% 100%, 0 100%); }

  .deal-list { position: absolute; left: 62px; top: 910px; list-style: disc; font-family: "Open Sans", sans-serif; font-weight: 700; font-size: 16px; line-height: 1.45; color: var(--ink); }
  .deal-list li { margin-left: 18px; }

  .contact { position: absolute; left: 500px; top: 918px; font-family: "Open Sans", sans-serif; font-size: 14px; line-height: 1.9; color: var(--ink); }
  .contact dt { float: left; clear: left; width: 70px; font-weight: 700; }
  .contact dd { margin-left: 70px; }
</style>
</head>
<body>
<main class="flyer">
  <svg class="decor" viewBox="0 0 849 1200" aria-hidden="true">
    <polygon points="400,0 849,0 849,40 470,70" fill="#7a1419"/>
    <polygon points="470,70 849,40 849,105" fill="#9c1b21"/>
    <polygon points="560,0 849,0 849,28" fill="#b3232a"/>
    <polygon points="0,1130 0,1200 170,1200" fill="#9c1b21"/>
    <polygon points="0,1165 0,1200 90,1200" fill="#7a1419"/>
    <polygon points="849,1095 849,1200 690,1200" fill="#9c1b21"/>
    <polygon points="849,1150 849,1200 780,1200" fill="#7a1419"/>
  </svg>

  <div class="brand">
    <span class="brand-mark" aria-hidden="true"></span>
    <span class="brand-name">Brelford Commercial</span>
  </div>

  <div class="title-banner"><h1>Join the Brelford Community</h1></div>

  <p class="tagline">Every member of Brelford Commercial is important to us,<br>be a part of our community and explore your neighborhood.</p>

  <div class="deal deal-row-1 deal-col-1">Receive a free month when you enroll!</div>
  <div class="deal deal-row-1 deal-col-2">Drop the sign-up fee.<span class="saving">Savings of $59</span></div>
  <div class="deal deal-row-1 deal-col-3">Purchase $25 and receive a free pair of Meadow Lane Boutique</div>
  <div class="deal deal-row-1 deal-col-4">BOGO FREE!</div>

  <div class="deal deal-row-2 deal-col-1">Buy a sandwich and receive a free Orbit shake</div>
  <div class="deal deal-row-2 deal-col-2">20% OFF Entire Service</div>
  <div class="deal deal-row-2 deal-col-3">Free Cookie Dough with regular pizza</div>
  <div class="deal deal-row-2 deal-col-4 deal-partner">
    <div class="partner-name">Tessa Marlow<span class="partner-badge"></span></div>
    <div>Free Nail Clipping with Pet Grooming</div>
  </div>

  <div class="section-tab deals-tab">Deals to implement:</div>
  <ul class="deal-list">
    <li>Brelford's: _ _ _ _ _ _</li>
    <li>Meadow Lane: _ _ _ _ _ _</li>
    <li>Orbit: _ _ _ _ _ _</li>
    <li>Summit mortgage: _ _ _ _ _ _</li>
    <li>Birchwood: _ _ _ _ _ _</li>
    <li>Nonna's: _ _ _ _ _ _</li>
  </ul>

  <div class="section-tab contact-tab">Contact Us:</div>
  <dl class="contact">
    <dt>Phone:</dt><dd>801.555.0147</dd>
    <dt>Website:</dt><dd>www.brelfordcommercial.example</dd>
    <dt>Address:</dt><dd>417 E. Dunmore Way Suite 5,<br>Centerville, UT 84099</dd>
  </dl>
</main>
</body>
</html>
```